Website design for an Italian restaurant in Amsterdam

I need a design for a client of mine. It is for Teatro Lunaverde, an Italian restaurant in Amsterdam.
We are going for a clean, modern look but we also need to realise an authentic feel.
The restaurant is located in an old movie theatre, that is where the name Teatro Lunaverde comes from.
Industry/Entity Type
Italian Restaurant
Number of Pages Required
1 page
Font styles to use
Sans Serif
Colors
Designer to choose colors to be used in the design.

```html
<!DOCTYPE html>
<html lang="en">
<head>
<meta charset="utf-8">
<title>Teatro Lunaverde</title>
<link rel="stylesheet" href="https://fonts.googleapis.com/css2?family=Montserrat:wght@300;400;500;600&display=swap">
<style>
  :root {
    --green: #0b5e3c;
    --green-dark: #084a2f;
    --ink: #555a5c;
    --white: #ffffff;
    --tan: #e9cfae;
    --tan-text: #ead4b8;
    --map-land: #dcdad6;
    --map-water: #8fb7d6;
  }
  * { box-sizing: border-box; margin: 0; padding: 0; }
  html, body { width: 742px; height: 1200px; overflow: hidden; background: var(--white); }
  body { font-family: "Montserrat", sans-serif; color: var(--ink); position: relative; }

  .site-header, .site-footer .footer-bar {
    height: 46px; display: flex; align-items: center; justify-content: space-between;
    padding: 0 93px 0 93px;
  }
  .brand { font-size: 16px; font-weight: 500; color: var(--green); letter-spacing: 0.2px; }
  .nav { display: flex; align-items: center; gap: 7px; font-size: 9.6px; font-weight: 400; color: #666; }
  .nav a { color: inherit; text-decoration: none; position: relative; }
  .nav a.current { color: #aaa; }
  .nav a.current::after {
    content: ""; position: absolute; left: 0; right: 0; bottom: -14px; height: 1.5px; background: var(--green);
  }
  .nav .btn-reserve {
    margin-left: 8px; background: var(--green); color: var(--white); padding: 6px 8px;
    border-radius: 3px; font-size: 9.6px;
  }

  .hero {
    position: absolute; top: 46px; left: 0; width: 742px; height: 372px;
    background:
      radial-gradient(ellipse at 25% 55%, rgba(190,90,140,0.35), transparent 35%),
      radial-gradient(ellipse at 80% 20%, rgba(30,28,40,0.85), transparent 45%),
      radial-gradient(ellipse at 70% 75%, rgba(40,45,90,0.7), transparent 45%),
      linear-gradient(180deg, #d9d6d3 0%, #b9b4ae 45%, #7a6254 80%, #9a6a45 100%);
    text-align: center;
  }
  .hero-text {
    position: absolute; top: 125px; left: 0; right: 0; font-size: 17.6px; font-weight: 400;
    line-height: 22px; color: rgba(255,240,230,0.62);
  }
  .btn {
    display: inline-flex; align-items: center; justify-content: center;
    background: var(--green); color: var(--white); font-size: 13px; font-weight: 400;
    border-radius: 3px; text-decoration: none;
  }
  .hero .btn { position: absolute; top: 250px; left: 302px; width: 139px; height: 37px; }

  .categories { position: absolute; top: 437px; left: 93px; display: flex; gap: 20px; }
  .category {
    width: 172px; height: 171px; border-radius: 8px; display: flex; align-items: center;
    justify-content: center; font-size: 28px; font-weight: 500; color: rgba(255,240,225,0.7);
  }
  .cat-dinner { background: radial-gradient(circle at 50% 50%, #c9673f, #8a4a28 70%, #6b3c22); }
  .cat-brunch { background: radial-gradient(circle at 50% 50%, #b9b3a8, #3a3a3c 55%, #1d1e21); }
  .cat-drinks { background: radial-gradient(circle at 40% 60%, #d2513a, #c89a94 55%, #e3dde0); }

  .celebration { position: absolute; top: 632px; left: 0; width: 742px; text-align: center; }
  .celebration h2 { font-size: 20.8px; font-weight: 500; color: var(--tan); }
  .celebration p { margin-top: 9px; font-size: 11.2px; font-weight: 500; line-height: 14px; color: var(--tan-text); }
  .celebration .btn { margin-top: 21px; width: 139px; height: 37px; }

  .visit {
    position: absolute; top: 763px; left: 0; width: 742px; height: 365px;
    background:
      radial-gradient(ellipse at 30% 60%, rgba(230,140,60,0.6), transparent 55%),
      radial-gradient(ellipse at 85% 80%, rgba(70,45,30,0.7), transparent 45%),
      linear-gradient(180deg, #6b4a33 0%, #b77a45 40%, #a3693c 70%, #5a3a26 100%);
  }
  .contact-info {
    position: absolute; left: 93px; top: 88px; color: rgba(255,255,255,0.9);
    font-size: 14.4px; font-weight: 400; line-height: 18.5px;
  }
  .contact-info .line { margin-bottom: 8px; }
  .contact-info .hours-title { margin-bottom: 9px; }
  .map {
    position: absolute; left: 372px; top: 91px; width: 278px; height: 261px;
    background: linear-gradient(120deg, var(--map-land) 0%, var(--map-land) 60%, #e4e2de 100%);
    border: 1px solid rgba(0,0,0,0.15);
  }
  .map-pin { position: absolute; left: 149px; top: 105px; }

  .site-footer { position: absolute; top: 1128px; left: 0; width: 742px; height: 72px; }
  .site-footer .footer-bar { height: 46px; }
  .copyright { position: absolute; top: 50px; left: 0; right: 0; text-align: center; font-size: 14px; color: #333; }
  .social { position: absolute; top: 46px; left: 515px; display: flex; gap: 8px; }
  .social span { width: 25px; height: 25px; border-radius: 50%; background: var(--green); display: block; }
</style>
</head>
<body>
  <header class="site-header">
    <div class="brand">Teatro Lunaverde</div>
    <nav class="nav">
      <a href="#">About</a><a href="#" class="current">Menu</a><a href="#">News</a><a href="#">Careers</a><a href="#">Gift Cards</a><a href="#">Contact</a>
      <a href="#" class="btn-reserve">Reservations</a>
    </nav>
  </header>

  <section class="hero" role="img" aria-label="Blurred restaurant interior with flowers in a vase on a table">
    <p class="hero-text">Lorem ipsum dolor sit amet, consectetur<br>adipisicing elit, sed do eiusmod tempor<br>incididunt ut labore et dolore magna</p>
    <a href="#" class="btn">See the menu</a>
  </section>

  <section class="categories">
    <div class="category cat-dinner" role="img" aria-label="Bruschetta with tomatoes on a wooden board">Dinner</div>
    <div class="category cat-brunch" role="img" aria-label="Plates of brunch dishes on a dark table">Brunch</div>
    <div class="category cat-drinks" role="img" aria-label="Red cocktails with mint garnish">Drinks</div>
  </section>

  <section class="celebration">
    <h2>Let us host your next celebration</h2>
    <p>Lorem ipsum dolor sit amet, consectetur adipisicing elit, sed do eiusmod<br>tempor incididunt ut labore et dolore magna aliqua. Ut enim ad minim</p>
    <a href="#" class="btn">Make reservation</a>
  </section>

  <section class="visit" role="img" aria-label="Close-up of a pizza, softly blurred">
    <div class="contact-info">
      <div class="line">1017 KX Amsterdam, Netherlands</div>
      <div class="line">(020) 555 - 0173</div>
      <div class="line hours-title">Hours of Operation:</div>
      <div>Mon – Thurs 9:00am – 11:00pm</div>
      <div>Fri 9:00am – Midnight</div>
      <div>Sat 9:00am – Midnight</div>
      <div>Sun 9:00pm - 11:00pm</div>
    </div>
    <div class="map" role="img" aria-label="Street map of the restaurant's neighbourhood">
      <svg class="map-pin" width="12" height="18" viewBox="0 0 12 18" aria-hidden="true">
        <path d="M6 0C2.7 0 0 2.6 0 5.9 0 10.3 6 18 6 18s6-7.7 6-12.1C12 2.6 9.3 0 6 0z" fill="#d93a2f"/>
        <circle cx="6" cy="6" r="2.2" fill="#8a1d16"/>
      </svg>
    </div>
  </section>

  <footer class="site-footer">
    <div class="footer-bar">
      <div class="brand">Teatro Lunaverde</div>
      <nav class="nav">
        <a href="#">About</a><a href="#">Menu</a><a href="#">News</a><a href="#">Careers</a><a href="#">Gift Cards</a><a href="#">Contact</a>
        <a href="#" class="btn-reserve">Reservations</a>
      </nav>
    </div>
    <div class="copyright">© 2018 Teatro Lunaverde</div>
    <div class="social" aria-label="Social links">
      <span></span><span></span><span></span><span></span>
    </div>
  </footer>
</body>
</html>
```